Brellham Pelvic Care Institute needs promo/informational brochure for marketing

Our practice has added a new practitioner and our goal is to highlight her (Lena Marsh, PA-C) in this marketing campaign while providing useful information about the practice and conditions we treat. We have also closed our Maryland Office and moved to a new NY office (9 E. 71st St. Suite 218 NY, NY 10021). I have included a copy of what our last brochure looked like as an example of what I absolutely despise:) We are removing Odette Klimer from the brochure and adding a book (also attached). We want something modern, concise, streamlined, and professional. We would love to see what you all can come up with! The sooner we get responses, the better!

Target Market(s)

physicians and patients

Industry/Entity Type

Medical

Font styles to use
Other font styles liked:
• avenir book? i'll leave it to the designer!

Colors
ffffff
cee9f5
e4daeb
000000
9d9d9d
cbcbcb

Requirements
Must have
• some sort of lotus image....or some type of background from stock images
• This is the bio of Lena Marsh to be included:
• Lena Marsh, PA
• Lena Marsh is a Nationally Certified Physician Assistant licensed in New York and Washington, DC. She graduated with honors from Pellingford School of Clinical Studies where she was awarded the prestigious Corvell Medal.
• Lena has been treating women with sexual dysfunction since 2010. She has extensive experience treating vaginismus, vulvodynia and other vulvovaginal disorders. She also has expertise in treating hypoactive sexual desire (low libido), arousal, and orgasmic disorders. Lena has lectured and written extensively on the topic of female sexual dysfunction and is a member of the Global Council on Intimate Wellness Research for Women.
• Lena practiced as a PA in psychiatry and orthopedic surgery before she became a female sexual medicine specialist. She is also a member of the Families of Overseas Servicemen Care Network and has volunteered in Vietnam providing medical care with Helping Hands Worldwide Relief (HHWR). Lena also studied at Garrick University in Australia and she spent two years living in Japan where she taught English with the Pacific Language Assistant Scheme.

```html
<!DOCTYPE html>
<html lang="en">
<head>
<meta charset="utf-8">
<title>Brellham Pelvic Care Institute – Brochure</title>
<link rel="stylesheet" href="https://fonts.googleapis.com/css2?family=Source+Sans+3:wght@300;400;600;700&display=swap">
<style>
:root{
  --white:#ffffff;
  --sky:#cee9f5;
  --lilac:#e4daeb;
  --ink:#000000;
  --grey:#9d9d9d;
  --silver:#cbcbcb;
  --stage:#a4a4a6;
  --rose:#e3bcd9;
  --band:#dbb6d0;
  --rule:#d9a7c9;
  --text:#2a2a2a;
}
*{margin:0;padding:0;box-sizing:border-box}
html,body{width:796px;height:1200px;overflow:hidden;background:var(--stage);font-family:"Source Sans 3",sans-serif;color:var(--text)}
.sheet{position:absolute;left:58px;width:682px;height:527px;display:flex;box-shadow:0 2px 6px rgba(0,0,0,.25)}
.sheet.outside{top:60px}
.sheet.inside{top:632px}
.panel{position:relative;isolation:isolate;width:227.33px;height:100%;overflow:hidden;
  background:linear-gradient(180deg,var(--white) 0%,#f1ecf5 35%,var(--lilac) 62%,#e6eef7 82%,var(--sky) 100%)}
.panel::after{content:"";position:absolute;top:0;bottom:0;right:0;width:28px;z-index:-1;background:linear-gradient(90deg,rgba(255,255,255,0),rgba(170,160,185,.18))}
.panel:last-child::after{display:none}
.panel-title{font-weight:300;font-size:19px;letter-spacing:.3px;text-transform:uppercase;color:#333;line-height:1}
.center{text-align:center}
.lotus{position:absolute;left:0;right:0;bottom:0;height:150px;z-index:-1;
  background:radial-gradient(ellipse 60% 45% at 50% 58%,rgba(150,140,190,.55),rgba(190,180,215,.35) 55%,rgba(255,255,255,0) 75%),
  radial-gradient(ellipse 90% 30% at 50% 90%,rgba(160,200,225,.5),rgba(255,255,255,0) 70%)}
.url{position:absolute;left:50%;transform:translateX(-50%);background:var(--rose);border-radius:8px;
  font-weight:700;font-size:10.5px;color:#111;padding:3px 20px;white-space:nowrap}
.url.plain{background:none}
.hr{height:1px;background:var(--rule);margin:0 14px}
.phone{display:flex;align-items:center;justify-content:center;gap:4px;font-size:12px;font-weight:600;color:#111;line-height:1.2}
.phone svg{width:10px;height:10px}
.small{font-size:6.4px;line-height:1.45}

/* locations */
.locations h1{margin-top:28px}
.loc-org{font-size:11px;line-height:1.35;margin:16px 0 12px;color:#222}
.office{padding:14px 0 12px}
.office h2{font-size:9.6px;font-weight:400;color:#111}
.office p{font-size:8px;line-height:1.4}
.office .note{font-size:6.4px;margin-top:8px;line-height:1.4}
.main-note{font-size:7.7px;line-height:1.45;padding:10px 16px 0}

/* books */
.books h1{margin:29px 0 14px;text-align:center}
.book{display:flex;gap:8px;padding:4px 8px 4px 12px;border-bottom:1px solid #e6d3e2;height:64px}
.book:last-child{border:none}
.cover{flex:0 0 42px;height:56px}
.book p{font-size:6px;line-height:1.4}
.contact{position:absolute;left:0;right:0;text-align:center}

/* front */
.front h1{margin:26px auto 0;width:180px;text-align:center;line-height:.98;font-size:20px}
.cities{margin:11px 16px 0;background:var(--band);font-size:9px;padding:2px 4px;color:#333;text-align:center}
.faces{display:flex;justify-content:center;gap:8px;margin:12px 0}
.face{width:56px;height:56px;border-radius:50%;background:radial-gradient(circle at 45% 40%,#cfcfcf,#6f6f6f);border:1px solid #fff}
.front .blurb{font-size:6.8px;line-height:1.6;text-align:center;padding:7px 22px}

/* inside */
.inside .panel-title{margin:26px 0 9px 18px;font-size:19px}
.intro{font-size:7.2px;line-height:1.45;padding:0 16px}
.treat-list{list-style:none;margin:14px 0 0 22px;font-size:7.4px;line-height:1.56}
.treat-list li::before{content:"•";margin-right:9px}
.philosophy ul{list-style:none;padding:0 14px 0 18px}
.philosophy li{font-size:7.2px;line-height:1.45;margin-bottom:13px;position:relative;padding-left:10px}
.philosophy li::before{content:"•";position:absolute;left:0}
.who .panel-title{margin-bottom:8px}
.bio{font-size:6.2px;line-height:1.4;padding:0 12px 0 18px;margin-bottom:7px}
.bio p+p{margin-top:3px}
.bio b{font-weight:700;color:#111}
.portrait{float:right;width:50px;height:50px;border-radius:50%;background:radial-gradient(circle at 45% 40%,#d8c4b4,#7c6a5e);margin:0 0 2px 4px;shape-outside:circle()}
</style>
</head>
<body>

<section class="sheet outside">
  <div class="panel locations center">
    <div class="lotus" role="img" aria-label="Lavender lotus flower resting on calm blue water"></div>
    <h1 class="panel-title">Locations</h1>
    <p class="loc-org">The Brellham Pelvic<br>Care Institute</p>
    <div class="hr"></div>
    <div class="office">
      <h2>Main Office</h2>
      <p>14 Larkmoor Circle NW, Suite 310<br>Washington, DC 20036<br>Phone: (202) 555-0148<br>Fax: (202) 555-0193</p>
      <p class="note">Across the street from<br>Alder Hill University Hospital<br>and the Larkmoor Metro</p>
    </div>
    <div class="hr"></div>
    <div class="office">
      <h2>New York Office:</h2>
      <p>9 E. 71st St. Suite 218<br>New York, NY 10021</p>
      <p class="note">Our newly opened office<br>on the Upper East Side</p>
    </div>
    <div class="hr"></div>
    <p class="main-note">Our office in Washington DC is our main office and all appointments and communications with both offices are made through this office.</p>
  </div>

  <div class="panel books">
    <div class="lotus" role="img" aria-label="Lavender lotus flower resting on calm blue water"></div>
    <h1 class="panel-title">Our Books</h1>
    <div class="book">
      <div class="cover" role="img" aria-label="Book cover in soft cream and green" style="background:linear-gradient(#f1efd6,#dfe6c4)"></div>
      <p>When Intimacy Aches is a guide for patients that contains up-to-date information on the diagnosis and treatment of more than 20 different causes of sexual and vulvovaginal pain. It contains an algorithm that helps a patient and her health care provider determine the specific cause and treatments of her type of vulvar pain.</p>
    </div>
    <div class="book">
      <div class="cover" role="img" aria-label="Book cover in deep blue tones" style="background:linear-gradient(#1f3a55,#4d6f8e)"></div>
      <p>Pelvic Pain in Women: Assessment and Care is the only textbook devoted to the diagnosis and treatment of vulvar and vaginal pain disorders and disease. More than 75 worldrenowned scientists contributed chapters in this authoritative and comprehensive textbook.</p>
    </div>
    <div class="book">
      <div class="cover" role="img" aria-label="Book cover in pale aqua tones" style="background:linear-gradient(#e9f3f4,#bcd9dc)"></div>
      <p>Renewing Desire: 4 Steps to Restoring Your Libido outlines a highly effective holistic approach to treating decreased sexual desire. In addition, there is essential information on the ways in which major life events such as pregnancy, menopause, and divorce can affect a woman's sexual health.</p>
    </div>
    <div class="book">
      <div class="cover" role="img" aria-label="Book cover in warm red tones" style="background:linear-gradient(#b83a3a,#d86a64)"></div>
      <p>Partnership: The Hidden History explains our non-monogamous instincts from an evolutionary perspective. Men and women are guided with compassion and wisdom in understanding their natural sexual tendencies to allow them to cultivate more lovemaking, even in long-term, monogamous relationships!</p>
    </div>
    <div class="book">
      <div class="cover" role="img" aria-label="Book cover in white and pink" style="background:linear-gradient(#f6f2f4,#e79ab8)"></div>
      <p>100 Answers About Vulvar and Vaginal Cancer and Other Diseases of the Vulva and Vagina provides practical, authoritative answers to the most common questions asked by women diagnosed with cancer of the vulva/vagina and related gynecologic diseases.</p>
    </div>
    <div class="contact" style="top:434px">
      <p class="small">9 E. 71st St. Suite 218 NY<br>NY 10021</p>
      <div class="phone"><svg viewBox="0 0 24 24"><path fill="#111" d="M6.6 10.8a15.1 15.1 0 0 0 6.6 6.6l2.2-2.2a1 1 0 0 1 1-.24 11.4 11.4 0 0 0 3.6.57 1 1 0 0 1 1 1V20a1 1 0 0 1-1 1A17 17 0 0 1 3 4a1 1 0 0 1 1-1h3.5a1 1 0 0 1 1 1c0 1.25.2 2.45.57 3.57a1 1 0 0 1-.25 1z"/></svg>(202) 555-0148</div>
    </div>
    <span class="url" style="top:480px">www.brellhampelvic.org</span>
  </div>

  <div class="panel front">
    <div class="lotus" role="img" aria-label="Lavender lotus flower resting on calm blue water"></div>
    <h1 class="panel-title">The Brellham Pelvic Care Institute</h1>
    <div class="cities">Washington DC &nbsp; New York City</div>
    <div class="faces">
      <div class="face" role="img" aria-label="Portrait photo of a smiling woman"></div>
      <div class="face" role="img" aria-label="Portrait photo of a smiling woman"></div>
      <div class="face" role="img" aria-label="Portrait photo of a smiling woman"></div>
    </div>
    <div class="hr"></div>
    <p class="blurb">For more than two decades, the Brellham Pelvic Care Institute has been a referral center for the treatment of vulvodynia, sexual pain disorders, dermatologic diseases of the vulva, recurrent vulvovaginal infections, and female sexual dysfunction.</p>
    <div class="hr"></div>
    <div class="faces">
      <div class="face" role="img" aria-label="Portrait photo of a smiling woman"></div>
      <div class="face" role="img" aria-label="Portrait photo of a smiling woman"></div>
      <div class="face" role="img" aria-label="Portrait photo of a smiling woman"></div>
    </div>
    <div class="contact" style="top:345px">
      <p class="small">9 E. 71st St. Suite 218 NY<br>NY 10021</p>
      <div class="phone"><svg viewBox="0 0 24 24"><path fill="#111" d="M6.6 10.8a15.1 15.1 0 0 0 6.6 6.6l2.2-2.2a1 1 0 0 1 1-.24 11.4 11.4 0 0 0 3.6.57 1 1 0 0 1 1 1V20a1 1 0 0 1-1 1A17 17 0 0 1 3 4a1 1 0 0 1 1-1h3.5a1 1 0 0 1 1 1c0 1.25.2 2.45.57 3.57a1 1 0 0 1-.25 1z"/></svg>(202) 555-0148</div>
    </div>
    <span class="url plain" style="bottom:8px">www.brellhampelvic.org</span>
  </div>
</section>

<section class="sheet inside">
  <div class="panel treat">
    <div class="lotus" role="img" aria-label="Lavender lotus flower resting on calm blue water"></div>
    <h1 class="panel-title">What We Treat</h1>
    <p class="intro">The physicians of the Brellham Pelvic Care Institute are experts in the diagnosis and treatment of more than two dozen diseases that cause the symptoms of genital itching, burning, irritation, rawness, throbbing, urinary frequency and urgency, and pain during sex. The diseases we treat include:</p>
    <ul class="treat-list">
      <li>Pain With Sex</li><li>Vaginal and Vulvar Discomfort</li><li>Burning, Rawness, Itching &amp; Pain</li><li>Vulvodynia</li><li>Vulvar Vestibulitis (Vestibulodynia)</li><li>Vulvovaginal Skin Diseases</li><li>Lichen Sclerosus</li><li>Lichen Planus</li><li>VIN</li><li>Lichen Simplex Chronicus</li><li>Plasma Cell Vulvitis</li><li>Pudendal Neuralgia</li><li>Chronic Pelvic Pain</li><li>Persistant Genital Arousal Disorder</li><li>Decreased Libido</li><li>Decreased Orgasm</li><li>Decreased Arousal</li><li>Pelvic Floor Muscle Dysfunction</li><li>Vaginismus</li><li>Interstitial Cystitis/Painful Bladder Syndrome</li>
    </ul>
    <span class="url" style="top:468px">www.brellhampelvic.org</span>
  </div>

  <div class="panel philosophy">
    <div class="lotus" role="img" aria-label="Lavender lotus flower resting on calm blue water"></div>
    <h1 class="panel-title">Our Philosophy</h1>
    <ul>
      <li>It is our belief that quality medical care cannot be rushed. By taking a comprehensive medical history, we give our patients the opportunity to be heard.</li>
      <li>We pride ourselves on our precise physical examinations, diagnostic precision and effective treatment. With the use of specialized testing and extensive research, we have developed algorithms to achieve accuracy and specificity in our diagnoses and therapies.</li>
      <li>Patient education is critical to our treatment process. We ensure that our patients have their questions answered and are guided with reliable resources. As a result, our patients are given a sense of hope and empowerment.</li>
      <li>We believe in the importance of experience and expertise. It is imperative for us to stay current with the latest literature, to focus our attention exclusively on vulvovaginal disorders and to invest a great deal of our own time and resources on research. We conduct over a dozen medical studies each year to find new treatments for vulvovaginal diseases.</li>
      <li>In our effort to provide the best care possible, we employ a multidisciplinary approach to treatment. To accomplish this, we enlist the help of our colleagues in other arenas of sexual health care including physical therapists, sex therapists, psychologists, and nutritionists.</li>
    </ul>
  </div>

  <div class="panel who">
    <div class="lotus" role="img" aria-label="Lavender lotus flower resting on calm blue water"></div>
    <h1 class="panel-title" style="margin-top:28px">Who We Are</h1>
    <div class="bio"><div class="portrait" role="img" aria-label="Portrait photo of a male physician in a suit"></div><p><b>Dr. Martin Hale</b> has been the director of the BPCI since 2002. He is the current President of the Global Council on Intimate Wellness Research for Women. In addition, he is a Fellow of IVDS, ACPS, and STRA. Dr. Hale has been a grant recipient of the National Vulvar Pain Alliance. He is actively involved in research and has published more than 75 abstracts, peer-reviewed articles, and book chapters. He is also co-author of When Intimacy Aches, Pelvic Pain in Women, and Renewing Desire.</p></div>
    <div class="bio"><div class="portrait" role="img" aria-label="Portrait photo of a female physician"></div><p><b>Dr. Nadia Ferro</b> completed her Ob/Gyn residency at Ashbury Medical and also completed a fellowship in Female Pelvic Medicine and Reconstructive Surgery at Renford University. She is regarded as an expert in the evaluation and treatment of female pelvic floor disorders and interstitial cystitis.</p></div>
    <div class="bio"><div class="portrait" role="img" aria-label="Portrait photo of a female physician assistant"></div>
      <p><b>Lena Marsh, PA</b> is a Nationally Certified Physician Assistant licensed in New York and Washington, DC. She graduated with honors from Pellingford School of Clinical Studies where she was awarded the prestigious Corvell Medal.</p>
      <p>Lena has been treating women with sexual dysfunction since 2010. She has extensive experience treating vaginismus, vulvodynia and other vulvovaginal disorders. She also has expertise in treating hypoactive sexual desire (low libido), arousal, and orgasmic disorders. Lena has lectured and written extensively on the topic of female sexual dysfunction and is a member of the Global Council on Intimate Wellness Research for Women.</p>
      <p>Lena practiced as a PA in psychiatry and orthopedic surgery before she became a female sexual medicine specialist. She is also a member of the Families of Overseas Servicemen Care Network and has volunteered in Vietnam providing medical care with Helping Hands Worldwide Relief (HHWR). Lena also studied at Garrick University in Australia and she spent two years living in Japan where she taught English with the Pacific Language Assistant Scheme.</p>
    </div>
    <span class="url" style="top:490px">www.brellhampelvic.org</span>
  </div>
</section>

</body>
</html>
```